Harbourgate Earthmoving – Website Design Brief

Web Design Brief

We are seeking a web designer to build a modern, responsive website for Harbourgate Earthmoving, a Sydney-based earthworks and excavation company.

2. Project Goal
- Build a professional, easy-to-navigate website that:
- Showcases HGE’s capabilities and past projects
- Attracts residential and commercial developers
- Builds credibility and encourages enquiries

3. Target Audience
- Residential developers and home builders
- Commercial construction firms
- Project managers seeking reliable excavation & plant hire services

4. Services to Highlight
- Bulk Excavation
- Detailed Excavation
- Demolition
- Shoring
- Plant Hire

5. Brand Style & Tone
- Clean, bold, and modern
- Professional with a “we get the job done” attitude
- Colors: Lime Green + Concrete Grey (from logo)
- Fonts: Match the modern, rounded, bold typeface in the logo
- Imagery: Showcase big machines, on-site work, before & after shots

6. Website Pages
Recommended structure:
- Home – Quick intro, project highlights, CTA
- About Us – Team story, mission, safety focus
- Services – Separate sections for each core service
- Projects – Case studies or photo gallery
- Plant Hire – Machines available, specs/photos
- Contact – Form + map + details

7. Assets Provided
- Logo (both long + stacked formats)
- Project photos. More can be provided if required.
- Copy: To be drafted

8. Deliverables
Responsive website (desktop/mobile/tablet)
- SEO-ready structure
- CMS (WordPress) for future edits
- Google Maps integration, job enquiry form

Target Market(s)

Target Audience Residential developers and home builders Commercial construction firms Project managers seeking reliable excavation & plant hire services

Industry/Entity Type

Construction

Number of Pages Required

1 page

Requirements
Must have
• Build a professional, easy-to-navigate website that: Showcases HGE’s capabilities and past projects Attracts residential and commercial developers Builds credibility and encourages enquiries
Nice to have
• All provided in the Description
Should not have

```html
<!DOCTYPE html>
<html lang="en">
<head>
<meta charset="utf-8">
<title>Harbourgate Earthmoving</title>
<link href="https://fonts.googleapis.com/css2?family=Outfit:wght@300;400;500;600;700;800&display=swap" rel="stylesheet">
<style>
:root{
  --green:#7dc243;
  --green-dark:#6aad33;
  --mint:#f4fde6;
  --ink:#1b1b1b;
  --body:#555;
  --white:#fff;
  --footer:#1c1c1c;
}
*{margin:0;padding:0;box-sizing:border-box}
html,body{width:1200px;height:4100px;overflow:hidden}
body{position:relative;font-family:"Outfit",sans-serif;color:var(--ink);background:var(--white)}
.abs{position:absolute}
.btn{position:absolute;display:flex;align-items:center;justify-content:center;background:var(--green);color:var(--white);border-radius:30px;font-weight:500;font-size:19px;letter-spacing:.3px;text-decoration:none}
.photo,.tile{position:absolute;box-shadow:inset 0 0 60px rgba(0,0,0,.18)}

/* nav */
.site-header{position:absolute;left:0;top:0;width:1200px;height:76px;background:var(--white)}
.brand{position:absolute;left:50px;top:28px;font-weight:600;font-size:20px;letter-spacing:1.2px;color:var(--green);white-space:nowrap}
.nav{position:absolute;top:31px;font-size:15px;font-weight:400;color:var(--ink)}
.nav.active{color:var(--green)}
.nav-cta{left:1014px;top:21px;width:142px;height:38px;font-size:15px}

/* hero */
.hero{position:absolute;left:0;top:76px;width:1200px;height:630px;background:linear-gradient(100deg,#646464 0%,#7a7a7a 30%,#8c98a6 48%,#9fbad6 62%,#bcd2e6 74%,#b59a7c 88%,#8a6a4e 100%)}
.hero-title{position:absolute;left:65px;top:178px;font-size:60px;font-weight:700;line-height:1.12;color:var(--white);white-space:nowrap}
.hero-text{position:absolute;left:65px;top:332px;width:440px;font-size:11px;line-height:1.3;color:#eee}
.hero-btn{left:53px;top:401px;width:167px;height:41px;font-size:18px}

/* about */
.about-photo{left:145px;top:744px;width:366px;height:366px;border-radius:50%;border:6px solid var(--green);background:radial-gradient(circle at 42% 38%,#e0b548 0%,#b08a34 30%,#6f5a38 60%,#8a8a86 85%,#5a5753 100%)}
.section-title{position:absolute;font-size:50px;font-weight:700;color:var(--ink);letter-spacing:.3px;white-space:nowrap}
.about-text{position:absolute;left:557px;top:883px;width:540px;font-size:13.5px;line-height:1.3;color:var(--body)}
.about-btn{left:550px;top:1014px;width:183px;height:45px}

/* services */
.services-bg{position:absolute;left:0;top:1189px;width:1200px;height:859px;background:var(--mint)}
.services-sub{position:absolute;left:153px;top:1490px;width:540px;font-size:13.5px;line-height:1.3;color:var(--body)}
.services-btn{left:851px;top:1469px;width:184px;height:47px}
.service-card{top:1601px;width:276px;height:321px}
.service-label{position:absolute;top:1938px;width:276px;text-align:center;font-size:20px;font-weight:600}
.arrow{position:absolute;width:60px;height:60px}

/* portfolio */
.portfolio-btn{left:499px;top:2891px;width:183px;height:46px}

/* testimonials */
.testimonial-text{position:absolute;left:326px;top:3436px;width:540px;text-align:center;font-size:13.5px;line-height:1.75;color:var(--white)}
.avatar{position:absolute;left:539px;top:3306px;width:108px;height:108px;border-radius:50%;background:radial-gradient(circle at 50% 40%,#b48e74 0%,#7d6656 45%,#3b4654 100%);border:3px solid rgba(255,255,255,.7)}
.testimonial-name{position:absolute;left:400px;top:3548px;width:392px;text-align:center;font-size:23px;font-weight:500;color:var(--white)}
.stars{position:absolute;left:530px;top:3596px}

/* footer */
.site-footer{position:absolute;left:0;top:3668px;width:1200px;height:432px;background:var(--footer);color:var(--white)}
.footer-brand{position:absolute;left:91px;top:118px;width:141px;height:102px;background:var(--white);display:flex;flex-direction:column;justify-content:center;align-items:center;color:var(--green);font-weight:600;font-size:16px;line-height:1.15;letter-spacing:1px}
.social{position:absolute;top:254px;width:20px;height:20px;border-radius:50%;background:var(--white)}
.footer-heading{position:absolute;font-size:19px;font-weight:700;letter-spacing:.3px}
.quick-link{position:absolute;left:488px;font-size:19px;display:flex;align-items:center;gap:9px}
.contact-item{position:absolute;left:830px;font-size:20px;display:flex;align-items:center;gap:16px}
.footer-rule{position:absolute;left:91px;top:352px;width:1028px;height:1px;background:#555}
.legal{position:absolute;top:386px;font-size:16px}
</style>
</head>
<body>

<header class="site-header">
  <div class="brand">HARBOURGATE EARTHMOVING</div>
  <a class="nav active" style="left:429px">HOME</a>
  <a class="nav" style="left:515px">ABOUT</a>
  <a class="nav" style="left:611px">SERVICES</a>
  <a class="nav" style="left:728px">PROJECTS</a>
  <a class="nav" style="left:851px">PLANT HIRE</a>
  <a class="btn nav-cta">CONTACT US</a>
</header>

<section class="hero" role="img" aria-label="Excavator dumping soil against a bright blue sky"></section>
<svg class="abs" style="left:0;top:560px" width="1200" height="150" viewBox="0 560 1200 150">
  <polygon points="0,706 347,604 1200,706" fill="#fff"/>
  <polygon points="0,566 347,604 0,706" fill="#7dc243"/>
</svg>
<h1 class="hero-title">HARBOURGATE<br>EARTHMOVING</h1>
<p class="hero-text">Bulk excavation, demolition, shoring and plant hire across Sydney. Skilled operators, modern machines and sites delivered safe, on time and ready for the next trade.</p>
<a class="btn hero-btn">GET A QUOTE</a>

<section>
  <div class="photo about-photo" role="img" aria-label="Close view of a yellow excavator bucket on site"></div>
  <h2 class="section-title" style="left:557px;top:810px">ABOUT US</h2>
  <p class="about-text">Lorem ipsum dolor sit amet, consectetur adipiscing elit, sed do eiusmod tempor incididunt ut labore et dolore magna aliqua. Ut enim ad minim veniam, quis nostrud xercitation ullamco laboris nisi ut aliquip ex ea commodo consequat. Duis aute irure dolor in reprehenderit in voluptate velit esse cillum dolore eu fugiat nulla pariatur. Excepteur sint occaecat cupidatat non proident, sunt in culpa qui officia deserunt mollit anim id est laborum.</p>
  <a class="btn about-btn">READ MORE</a>
</section>

<section>
  <div class="services-bg"></div>
  <svg class="abs" style="left:0;top:1189px" width="1200" height="141" viewBox="0 1189 1200 141">
    <polygon points="811,1272 1200,1189 1200,1329" fill="#7dc243"/>
  </svg>
  <h2 class="section-title" style="left:153px;top:1418px">OUR SERVICES</h2>
  <p class="services-sub">Lorem ipsum dolor sit amet, consectetur adipiscing elit, sed do eiusmod tempor incididunt ut labore et dolore magna aliqua.</p>
  <a class="btn services-btn">VIEW ALL</a>

  <svg class="arrow" style="left:56px;top:1740px" viewBox="0 0 60 60"><circle cx="30" cy="30" r="28.5" fill="none" stroke="#7dc243" stroke-width="2"/><polyline points="35,17 22,30 35,43" fill="none" stroke="#7dc243" stroke-width="2.5"/></svg>
  <svg class="arrow" style="left:1069px;top:1740px" viewBox="0 0 60 60"><circle cx="30" cy="30" r="28.5" fill="none" stroke="#7dc243" stroke-width="2"/><polyline points="25,17 38,30 25,43" fill="none" stroke="#7dc243" stroke-width="2.5"/></svg>

  <div class="photo service-card" style="left:153px;background:linear-gradient(150deg,#5e4c2c 0%,#d4a93e 25%,#a9842f 45%,#6b5a3c 70%,#9a9690 100%)" role="img" aria-label="Yellow excavator arm and bucket"></div>
  <div class="photo service-card" style="left:459px;background:linear-gradient(180deg,#5d7a4c 0%,#4c5a44 20%,#8b7052 40%,#b68a5a 70%,#9a7550 100%)" role="img" aria-label="Excavator clearing a demolition site"></div>
  <div class="photo service-card" style="left:765px;background:linear-gradient(180deg,#fff3cf 0%,#f1d88c 25%,#d8b25a 45%,#9aa06a 70%,#5f8a3c 100%)" role="img" aria-label="Yellow excavator parked on grass at sunset"></div>
  <div class="service-label" style="left:153px">Bulk Excavation</div>
  <div class="service-label" style="left:459px">Demolition</div>
  <div class="service-label" style="left:765px">Plant Hire</div>
</section>

<section>
  <h2 class="section-title" style="left:0;width:1217px;text-align:center;top:2148px">OUR PORTFOLIO</h2>
  <div class="tile" style="left:134px;top:2291px;width:294px;height:166px;background:linear-gradient(180deg,#6e7378 0%,#c4c7cb 28%,#f1f2f3 50%,#9a9c9f 72%,#2b2b2d 100%)" role="img" aria-label="Company ute parked on a street"></div>
  <div class="tile" style="left:134px;top:2469px;width:294px;height:356px;background:linear-gradient(180deg,#2f4a2c 0%,#486a40 30%,#8f9a8a 48%,#e6e6e4 62%,#bcbcbc 78%,#242424 100%)" role="img" aria-label="Tipper truck beside trees"></div>
  <div class="tile" style="left:447px;top:2291px;width:294px;height:355px;background:linear-gradient(180deg,#a9b2bc 0%,#c8ccd0 25%,#d4ad2e 45%,#e2e2e0 62%,#8d7b68 82%,#6b5d50 100%)" role="img" aria-label="Excavator loading a truck at a demolition site"></div>
  <div class="tile" style="left:447px;top:2658px;width:294px;height:167px;background:linear-gradient(180deg,#6f86a0 0%,#9a5a3e 40%,#7e4a34 65%,#6b6a58 100%)" role="img" aria-label="Brick house behind site fencing"></div>
  <div class="tile" style="left:765px;top:2291px;width:294px;height:166px;background:linear-gradient(170deg,#6c5c40 0%,#a88451 40%,#c9a06a 65%,#8d6f48 100%)" role="img" aria-label="Excavated footings in sandy ground"></div>
  <div class="tile" style="left:765px;top:2469px;width:294px;height:356px;background:linear-gradient(160deg,#9a8c78 0%,#6e6458 35%,#3f3a35 55%,#7d7265 80%,#968a7a 100%)" role="img" aria-label="Excavator track on compacted dirt"></div>
  <a class="btn portfolio-btn">VIEW ALL</a>
</section>

<section>
  <svg class="abs" style="left:0;top:2997px" width="1200" height="671" viewBox="0 2997 1200 671">
    <polygon points="811,3093 1200,2997 1200,3140" fill="#1c1c1c"/>
    <polygon points="0,2997 811,3093 1200,3140 1200,3668 0,3668" fill="#7dc243"/>
  </svg>
  <div class="abs" style="left:0;top:2997px;width:1200px;height:671px;background:linear-gradient(90deg,rgba(60,100,30,.28) 0%,rgba(140,200,80,.05) 40%,rgba(140,200,80,.05) 60%,rgba(60,100,30,.28) 100%);clip-path:polygon(0 0,811px 96px,1200px 143px,1200px 671px,0 671px)" role="img" aria-label="Green tinted view of a site with parked machinery"></div>
  <h2 class="section-title" style="left:0;width:1187px;text-align:center;top:3195px;color:#fff">TESTIMONIALS</h2>
  <div class="avatar" role="img" aria-label="Client portrait"></div>
  <svg class="arrow" style="left:126px;top:3412px" viewBox="0 0 60 60"><circle cx="30" cy="30" r="28.5" fill="none" stroke="#fff" stroke-width="2"/><polyline points="35,17 22,30 35,43" fill="none" stroke="#fff" stroke-width="2.5"/></svg>
  <svg class="arrow" style="left:1005px;top:3417px" viewBox="0 0 60 60"><circle cx="30" cy="30" r="28.5" fill="none" stroke="#fff" stroke-width="2"/><polyline points="25,17 38,30 25,43" fill="none" stroke="#fff" stroke-width="2.5"/></svg>
  <p class="testimonial-text">Lorem ipsum dolor sit amet, consectetur adipiscing elit, sed do eiusmod tempor incididunt ut labore et dolore magna aliqua. Ut enim ad minim veniam, quis nostrud xercitation ullamco laboris nisi ut aliquip ex ea commodo consequat. Duis aute irure dolor in reprehenderit in voluptate.</p>
  <div class="testimonial-name">SAM KELLERMAN</div>
  <svg class="stars" width="130" height="24" viewBox="0 0 130 24">
    <g fill="#f5b82e">
      <polygon points="12,1 15,9 23,9 16.5,14 19,22 12,17 5,22 7.5,14 1,9 9,9"/>
      <polygon transform="translate(26 0)" points="12,1 15,9 23,9 16.5,14 19,22 12,17 5,22 7.5,14 1,9 9,9"/>
      <polygon transform="translate(52 0)" points="12,1 15,9 23,9 16.5,14 19,22 12,17 5,22 7.5,14 1,9 9,9"/>
      <polygon transform="translate(78 0)" points="12,1 15,9 23,9 16.5,14 19,22 12,17 5,22 7.5,14 1,9 9,9"/>
      <polygon transform="translate(104 0)" points="12,1 15,9 23,9 16.5,14 19,22 12,17 5,22 7.5,14 1,9 9,9"/>
    </g>
  </svg>
</section>

<footer class="site-footer">
  <div class="footer-brand"><span>HARBOURGATE</span><span>EARTHMOVING</span></div>
  <span class="social" style="left:90px" aria-label="Social profile"></span>
  <span class="social" style="left:156px" aria-label="Social profile"></span>
  <span class="social" style="left:225px" aria-label="Social profile"></span>

  <div class="footer-heading" style="left:484px;top:104px">QUICK LINKS</div>
  <div class="quick-link" style="top:142px"><svg width="16" height="16" viewBox="0 0 16 16"><circle cx="8" cy="8" r="6.5" fill="none" stroke="#7dc243" stroke-width="1.5"/><polyline points="6,5 9,8 6,11" fill="none" stroke="#7dc243" stroke-width="1.5"/></svg>Home</div>
  <div class="quick-link" style="top:179px"><svg width="16" height="16" viewBox="0 0 16 16"><circle cx="8" cy="8" r="6.5" fill="none" stroke="#7dc243" stroke-width="1.5"/><polyline points="6,5 9,8 6,11" fill="none" stroke="#7dc243" stroke-width="1.5"/></svg>About</div>
  <div class="quick-link" style="top:216px"><svg width="16" height="16" viewBox="0 0 16 16"><circle cx="8" cy="8" r="6.5" fill="none" stroke="#7dc243" stroke-width="1.5"/><polyline points="6,5 9,8 6,11" fill="none" stroke="#7dc243" stroke-width="1.5"/></svg>Services</div>
  <div class="quick-link" style="top:252px"><svg width="16" height="16" viewBox="0 0 16 16"><circle cx="8" cy="8" r="6.5" fill="none" stroke="#7dc243" stroke-width="1.5"/><polyline points="6,5 9,8 6,11" fill="none" stroke="#7dc243" stroke-width="1.5"/></svg>Projects</div>
  <div class="quick-link" style="top:289px"><svg width="16" height="16" viewBox="0 0 16 16"><circle cx="8" cy="8" r="6.5" fill="none" stroke="#7dc243" stroke-width="1.5"/><polyline points="6,5 9,8 6,11" fill="none" stroke="#7dc243" stroke-width="1.5"/></svg>Contact</div>

  <div class="footer-heading" style="left:831px;top:96px">CONTACT INFO</div>
  <div class="contact-item" style="top:140px"><svg width="28" height="28" viewBox="0 0 24 24"><path fill="#7dc243" d="M6.6 10.8c1.4 2.8 3.8 5.1 6.6 6.6l2.2-2.2c.3-.3.7-.4 1-.2 1.1.4 2.3.6 3.6.6.6 0 1 .4 1 1V20c0 .6-.4 1-1 1C10.6 21 3 13.4 3 4c0-.6.4-1 1-1h3.5c.6 0 1 .4 1 1 0 1.3.2 2.5.6 3.6.1.3 0 .7-.2 1z"/></svg>(02) 5550 1847</div>
  <div class="contact-item" style="top:208px"><svg width="28" height="24" viewBox="0 0 28 24"><rect x="1" y="5" width="26" height="18" rx="2" fill="#7dc243"/><polyline points="1,6 14,15 27,6" fill="none" stroke="#1c1c1c" stroke-width="2"/></svg>hello@harbourgate.example</div>
  <div class="contact-item" style="top:280px"><svg width="24" height="30" viewBox="0 0 24 30"><path fill="#7dc243" d="M12 1C6 1 2 5.5 2 11c0 7 10 18 10 18s10-11 10-18C22 5.5 18 1 12 1z"/><circle cx="12" cy="11" r="4" fill="#1c1c1c"/></svg>14 Quarry Rd, Marrickville</div>

  <div class="footer-rule"></div>
  <div class="legal" style="left:91px">Copyright © 2025, All Rights Reserved.</div>
  <div class="legal" style="left:845px">Privacy Policy | Term &amp; Conditions</div>
</footer>

</body>
</html>
```